QRV Consulting Web Design… We need a Facelift!

We currently have a website but it is very outdated. We like our content, but could use some help on giving it a refreshed facelift.

www.QRV-Consulting.example is our site

We only consult with large companies in the US that have sales over $250,000 a year, so looking to be high end yet approachable in our look.

Target Market(s)

Large corporations

Industry/Entity Type

Consulting

Coding

Coded - Design and coding required

Number of Pages Required

5+ page

Font styles to use
Serif
Sans Serif

Requirements
Must have
• We love our logo, keep that the same.
• The site colors can deviate from the logo, as long as it is complimentary
Nice to have
• We like our videos and graphics. If you can make them better, then great! But you can also feel free to reuse them.
• There is a video on the opening screen and one on the video page.
• We would like the video on the video page to be incorporated on the first page.
• If you think we need other/more page, we are all ears!
Should not have
• Want to set us apart from our competition in look, feel, professionalism and step away from the old fashioned conservatives of their websites. We want to be professional, yet bolder and fresher.
• Our Competition is LedgerPilot.example and TheBrindlewoodGroup.example, but not looking to copy of emulate them, but gives an idea of the world QRV is in.

```html
<!DOCTYPE html>
<html lang="en">
<head>
<meta charset="utf-8">
<title>QRV Consulting</title>
<link href="https://fonts.googleapis.com/css2?family=Open+Sans:wght@400;600;700;800&family=Jura:wght@400;500&family=Exo+2:wght@800;900&display=swap" rel="stylesheet">
<style>
:root{
  --red:#a3180b;
  --red-dark:#8e1207;
  --red-mid:#b92a1c;
  --red-light:#d6483d;
  --blue:#4aa3df;
  --ink:#1a1a1a;
  --dark:#222222;
  --footer:#1f1f1f;
  --black:#0c0c0c;
  --grey:#e6e6e6;
  --text:#555;
  --white:#fff;
}
*{margin:0;padding:0;box-sizing:border-box}
html,body{width:1200px;height:3309px;overflow:hidden}
body{position:relative;font-family:"Open Sans",Arial,sans-serif;color:var(--text);background:var(--white);font-size:13px}
.abs{position:absolute}
/* top bar */
.topbar{left:0;top:0;width:1200px;height:38px;background:var(--black);color:#ddd;font-size:12px}
.topbar .welcome{position:absolute;left:71px;top:11px}
.topbar .login{position:absolute;left:1013px;top:0;width:118px;height:38px;background:var(--red);color:#fff;font-weight:700;font-size:13px;text-align:center;line-height:38px}
/* header */
.header{left:0;top:38px;width:1200px;height:132px;background:#fff}
.logo{position:absolute;left:71px;top:28px;display:flex;align-items:center;gap:12px}
.logo .mark{width:46px;height:46px;border-radius:50%;background:var(--red)}
.logo .name{font-family:"Open Sans",sans-serif;font-weight:800;font-size:34px;color:var(--red);line-height:1}
.logo .sub{position:absolute;left:0;top:58px;font-size:13px;font-weight:600;color:#555;white-space:nowrap}
.contact{position:absolute;top:50px;display:flex;gap:10px;align-items:flex-start}
.contact .ico{width:38px;height:38px;background:var(--red);display:flex;align-items:center;justify-content:center}
.contact small{display:block;font-size:11px;color:#666}
.contact b{display:block;font-size:13px;color:var(--ink);font-weight:700}
/* nav */
.nav{left:0;top:170px;width:1200px;height:40px;background:var(--red)}
.nav ul{list-style:none;position:absolute;left:71px;top:0;display:flex;height:40px;align-items:center}
.nav li{color:#fff;font-size:13px;margin-right:44px}
.nav li.active{font-weight:700}
.search{position:absolute;left:920px;top:5px;width:202px;height:30px;background:#fff;font-size:11px;color:#aaa;padding:8px 10px}
.search svg{position:absolute;right:8px;top:7px}
/* hero */
.hero{left:0;top:210px;width:1200px;height:668px;background:linear-gradient(100deg,#8fbde9 0%,#a9c9e6 30%,#5f7890 55%,#2b3a4c 80%,#1a2330 100%)}
.hero h1{position:absolute;left:71px;top:160px;font-family:"Exo 2",sans-serif;font-weight:900;font-size:50px;color:var(--ink);letter-spacing:2px}
.hero p{position:absolute;left:71px;top:225px;width:430px;font-size:14px;line-height:22px;color:#1d2a3a}
.btn{display:inline-block;background:var(--red);color:#fff;font-weight:700;font-size:13px;text-align:center}
.hero .join{position:absolute;left:71px;top:353px;width:161px;height:46px;line-height:46px}
/* features */
.feature{top:816px;width:265px;height:212px;color:#fff;text-align:center}
.feature .circ{position:absolute;left:88px;top:-55px;width:88px;height:88px;border-radius:50%;border:3px solid #fff;display:flex;align-items:center;justify-content:center}
.feature h3{position:absolute;top:38px;left:10px;right:10px;font-size:17px;line-height:19px;font-weight:700}
.feature p{position:absolute;top:92px;left:40px;right:20px;font-size:12.5px;line-height:17px;text-align:left}
.feature .more{position:absolute;left:82px;top:160px;width:100px;height:34px;line-height:34px;background:#fff;color:var(--ink);font-weight:700;font-size:13px}
/* section heads */
.shead{left:0;width:1200px;text-align:center;font-family:"Jura",sans-serif;font-weight:400;font-size:44px;color:#333;letter-spacing:2px}
.shead::after{content:"";display:block;width:70px;height:3px;background:var(--red);margin:8px auto 0}
.quote{left:0;top:1148px;width:1200px;text-align:center;font-weight:700;font-size:14px;color:#333}
.quote span{color:var(--red);font-size:24px;vertical-align:-6px;margin:0 4px}
.who-p{left:150px;top:1186px;width:900px;text-align:center;font-size:12.5px;line-height:18px;color:#666}
/* video */
.video{left:71px;top:1275px;width:540px;height:335px;background:#111;padding:8px}
.video .frame{width:100%;height:288px;background:linear-gradient(135deg,#d8dde0,#9aa4a8 45%,#6d6a66 70%,#c9b8a5)}
.video .bar{position:absolute;left:8px;right:8px;bottom:8px;height:28px;display:flex;align-items:center;gap:14px;padding:0 10px;color:#fff;font-size:11px}
.video .prog{position:absolute;left:8px;right:8px;bottom:36px;height:3px;background:#555}
.video .prog i{display:block;width:8%;height:3px;background:var(--red)}
.intro{left:611px;top:1275px;width:520px;height:335px;background:var(--blue);color:#fff;padding:24px 24px}
.intro h2{font-weight:700;font-size:22px;line-height:30px;color:#111}
.intro p{font-size:12.5px;line-height:18px;margin-top:12px;color:#fff}
.intro p+p{margin-top:10px}
.intro .watch{margin:18px 0 0 8px;width:180px;height:46px;background:var(--red);display:flex;align-items:center;gap:12px;padding-left:10px;font-size:14px;font-weight:600}
/* band */
.band{left:0;top:1666px;width:1200px;height:150px;background:var(--dark)}
.band h2{position:absolute;left:71px;top:38px;width:820px;font-size:28px;line-height:36px;color:#fff;font-weight:700}
.band .team{position:absolute;left:955px;top:56px;width:176px;height:44px;line-height:44px;background:var(--blue);color:#111;font-weight:600;font-size:14px;text-align:center}
/* services */
.serv-sub{left:280px;top:1950px;width:640px;text-align:center;font-size:12.5px;line-height:18px;color:#666}
.service{top:2021px;width:242px;text-align:center}
.service .img{width:242px;height:198px}
.service .circ{width:72px;height:72px;border-radius:50%;background:var(--red);margin:-36px auto 0;position:relative;display:flex;align-items:center;justify-content:center}
.service .lead{font-size:12.5px;line-height:18px;color:#333;margin-top:8px;padding:0 10px}
.service h3{font-size:18px;font-weight:700;color:#111;margin-top:14px;white-space:nowrap}
.service p{font-size:12.5px;line-height:17px;color:#444;margin:8px auto 0;width:200px}
.service .btn{width:96px;height:36px;line-height:36px;margin-top:16px}
/* clients */
.clients{left:0;top:2526px;width:757px;height:452px;background:var(--grey);text-align:center}
.clients h2{position:absolute;top:36px;left:0;width:757px;font-family:"Jura",sans-serif;font-weight:400;font-size:44px;color:#222;letter-spacing:2px}
.clients h2::after{content:"";display:block;width:70px;height:3px;background:var(--red);margin:8px auto 0}
.clients .tag{position:absolute;top:118px;left:0;width:757px;font-weight:700;font-size:14px;color:#333}
.clients .avatar{position:absolute;left:337px;top:160px;width:104px;height:104px;border-radius:50%;background:radial-gradient(circle at 50% 40%,#e7dcd4 0 38%,var(--red) 40%)}
.clients .say{position:absolute;top:282px;left:90px;width:600px;font-size:12.5px;line-height:20px;color:#333}
.clients .who{position:absolute;top:340px;left:0;width:757px;font-weight:700;font-size:14px;color:#222}
.clients .role{position:absolute;top:364px;left:0;width:757px;font-size:13px;color:#333}
.clients .role span{color:var(--red)}
.dots{position:absolute;top:398px;left:0;width:757px;display:flex;justify-content:center;gap:5px}
.dots i{width:9px;height:9px;background:var(--red)}
.dots i.on{background:#333}
.feedback{left:757px;top:2526px;width:443px;height:452px;background:var(--red);color:#fff;padding:30px 22px}
.feedback h2{font-size:28px;line-height:34px;font-weight:700;width:320px}
.feedback p{font-size:12.5px;line-height:17px;margin-top:18px;width:320px}
.feedback .field{margin-left:35px;width:270px;height:42px;background:#fff;color:#aaa;font-size:12px;padding:12px 10px;margin-top:8px}
.feedback .first{margin-top:22px}
.feedback .area{height:74px}
.feedback .send{margin-left:35px;margin-top:12px;width:110px;height:42px;line-height:42px;background:var(--blue);color:#fff;font-weight:700;text-align:center;font-size:14px}
/* footer */
.footer{left:0;top:2978px;width:1200px;height:298px;background:var(--footer);color:#ddd}
.fcol{position:absolute;top:40px}
.fcol h4{color:var(--blue);font-size:20px;font-weight:700;margin-bottom:22px}
.fcol p{font-size:12.5px;line-height:19px;color:#ddd}
.fcol ul{list-style:none}
.fcol li{font-size:12.5px;line-height:29px;padding-left:16px;position:relative}
.fcol li::before{content:"";position:absolute;left:2px;top:13px;width:5px;height:5px;border-radius:50%;background:var(--blue)}
.fcol .inp{width:200px;height:36px;background:#fff;color:#999;font-size:12px;padding:10px 8px;margin-bottom:8px}
.fcol .inp.tall{height:68px}
.fcol .send{width:86px;height:30px;line-height:30px;background:var(--blue);color:#fff;font-weight:700;text-align:center;font-size:14px}
.crow{display:flex;gap:12px;align-items:flex-start;font-size:12.5px;line-height:18px;margin-top:16px}
.copy{left:0;top:3276px;width:1200px;height:33px;background:var(--black);color:#ccc;font-size:12px;text-align:center;line-height:33px}
</style>
</head>
<body>

<div class="abs topbar">
  <span class="welcome">Welcome visitor</span>
  <span class="login">Login Here</span>
</div>

<header class="abs header">
  <div class="logo">
    <span class="mark"></span>
    <span class="name">QRV</span>
    <span class="sub">QRV-Consulting.example</span>
  </div>
  <div class="contact" style="left:474px">
    <span class="ico"><svg width="18" height="18" viewBox="0 0 18 18"><rect x="2" y="4" width="14" height="11" fill="none" stroke="#fff" stroke-width="2"/><path d="M6 4V2h6v2" stroke="#fff" stroke-width="2" fill="none"/></svg></span>
    <div><small>Tips</small><b>Negotiating Bank Fees Tips</b></div>
  </div>
  <div class="contact" style="left:730px">
    <span class="ico"><svg width="18" height="18" viewBox="0 0 18 18"><path d="M4 2l3 3-2 2c1 2 3 4 5 5l2-2 3 3-2 3C8 16 2 10 2 4z" fill="#fff"/></svg></span>
    <div><small>Call Us</small><b>(555) 0140 227</b></div>
  </div>
  <div class="contact" style="left:890px">
    <span class="ico"><svg width="18" height="18" viewBox="0 0 18 18"><rect x="2" y="4" width="14" height="10" fill="#fff"/><path d="M2 4l7 6 7-6" stroke="#a3180b" stroke-width="1.5" fill="none"/></svg></span>
    <div><small>Email Us</small><b>Info@QRV-Consulting.example</b></div>
  </div>
</header>

<nav class="abs nav">
  <ul>
    <li class="active">Why QRV</li><li>Our Process</li><li>Contact Us</li><li>About Us</li><li>Client List</li>
  </ul>
  <div class="search">Search Site
    <svg width="16" height="16" viewBox="0 0 16 16"><circle cx="6.5" cy="6.5" r="4.5" fill="none" stroke="#333" stroke-width="2"/><path d="M10 10l4 4" stroke="#333" stroke-width="2"/></svg>
  </div>
</nav>

<section class="abs hero" role="img" aria-label="Photo of two businessmen reviewing documents at a desk">
  <h1>A BRAND-NEW</h1>
  <p>way to manage your treasury management feesway to manage your treasury management feesway to manage your treasury management feesway to manage your treasury management fees</p>
  <span class="btn join">JOIN US</span>
</section>

<div class="abs feature" style="left:71px;background:var(--red-light)">
  <div class="circ" style="background:var(--red-light)"><svg width="40" height="36" viewBox="0 0 40 36"><rect x="4" y="22" width="6" height="12" fill="#fff"/><rect x="14" y="16" width="6" height="18" fill="#fff"/><rect x="24" y="10" width="6" height="24" fill="#fff"/><path d="M4 16L16 6l8 6 12-10" stroke="#fff" stroke-width="2.5" fill="none"/></svg></div>
  <h3>Relationship Profitability Modeling</h3>
  <p>Lorem ipsum dolor sit amet, consectetur adipiscing elit. Aliquam quis semper felis.</p>
  <span class="more">Read More</span>
</div>
<div class="abs feature" style="left:336px;background:var(--red-mid)">
  <div class="circ" style="background:var(--red-mid)"><svg width="40" height="36" viewBox="0 0 40 36"><rect x="4" y="24" width="6" height="10" fill="#fff"/><rect x="14" y="18" width="6" height="16" fill="#fff"/><rect x="24" y="12" width="6" height="22" fill="#fff"/><path d="M6 16L30 4M24 3h7v7" stroke="#fff" stroke-width="2.5" fill="none"/></svg></div>
  <h3>Our<br>Process</h3>
  <p>Lorem ipsum dolor sit amet, consectetur adipiscing elit. Aliquam quis semper felis.</p>
  <span class="more">Read More</span>
</div>
<div class="abs feature" style="left:601px;background:var(--red)">
  <div class="circ" style="background:var(--red)"><svg width="40" height="38" viewBox="0 0 40 38"><circle cx="17" cy="12" r="8" fill="#fff"/><path d="M3 36c0-10 6-14 14-14s14 4 14 14z" fill="#fff"/><circle cx="31" cy="8" r="5" fill="none" stroke="#fff" stroke-width="2"/><path d="M29 8h4" stroke="#fff" stroke-width="2"/></svg></div>
  <h3>Treasury<br>Crawler</h3>
  <p>Lorem ipsum dolor sit amet, consectetur adipiscing elit. Aliquam quis semper felis.</p>
  <span class="more">Read More</span>
</div>
<div class="abs feature" style="left:866px;background:var(--red-dark)">
  <div class="circ" style="background:var(--red-dark)"><svg width="42" height="34" viewBox="0 0 42 34"><circle cx="21" cy="9" r="6" fill="#fff"/><circle cx="9" cy="12" r="4.5" fill="#fff"/><circle cx="33" cy="12" r="4.5" fill="#fff"/><path d="M11 32c0-9 4-14 10-14s10 5 10 14z" fill="#fff"/><path d="M1 30c0-7 3-10 8-10s8 3 8 10zM25 30c0-7 3-10 8-10s8 3 8 10z" fill="#fff"/></svg></div>
  <h3>Comparative Analysis Modeling</h3>
  <p>Lorem ipsum dolor sit amet, consectetur adipiscing elit. Aliquam quis semper felis.</p>
  <span class="more">Read More</span>
</div>

<h2 class="abs shead" style="top:1066px">WHO WE ARE</h2>
<p class="abs quote"><span>"</span>provide clarity and transparency to the treasury and cash management<span>"</span></p>
<p class="abs who-p">We are a consortium of ex-bankers, consultants, certified treasury professionals, and former practitioners that combined our resources with the objective of participating in a common activity for achieving a common goal: assisting clients in maximizing the return of their treasury and cash management relationships by uncovering details that typically only bankers know.</p>

<div class="abs video">
  <div class="frame" role="img" aria-label="Video still of a consultant working with a group of students at a laptop"></div>
  <div class="prog"><i></i></div>
  <div class="bar">
    <svg width="12" height="12" viewBox="0 0 12 12"><path d="M2 1l9 5-9 5z" fill="#fff"/></svg>
    <svg width="14" height="12" viewBox="0 0 14 12"><path d="M1 1l7 5-7 5zM9 1h2v10H9z" fill="#fff"/></svg>
    <svg width="14" height="12" viewBox="0 0 14 12"><path d="M1 4h3l4-3v10L4 8H1z" fill="#fff"/></svg>
    <span>0:12 / 2:51</span>
    <span style="flex:1"></span>
    <svg width="14" height="12" viewBox="0 0 14 12"><circle cx="7" cy="6" r="4" fill="none" stroke="#fff" stroke-width="2"/></svg>
    <svg width="16" height="12" viewBox="0 0 16 12"><rect x="1" y="1" width="14" height="10" fill="none" stroke="#fff" stroke-width="1.5"/></svg>
    <svg width="14" height="12" viewBox="0 0 14 12"><path d="M1 4V1h4M9 1h4v3M13 8v3H9M5 11H1V8" stroke="#fff" stroke-width="1.5" fill="none"/></svg>
  </div>
</div>
<div class="abs intro">
  <h2>Introducing a brand-new way tomanage your treasury management fees</h2>
  <p>QRV Consulting works closely with your team assisting in auditing your bank fees and earnings credit rates. As former bankers, we bring our primary and regional bank experience to the table to supplement your team</p>
  <p>In providing insider knowledge for various bank pricing and net cost thresholds, so you can negotiate better pricing rates, and terms.<br>Maximize return when you Manage Your Discount</p>
  <div class="watch"><svg width="28" height="28" viewBox="0 0 28 28"><circle cx="14" cy="14" r="13" fill="#fff"/><path d="M20 14H9M13 9l-5 5 5 5" stroke="#a3180b" stroke-width="2.5" fill="none"/></svg>Check Our Video</div>
</div>

<section class="abs band">
  <h2>We are a consortium of ex-bankers, consultants, certified treasury professionals, and former</h2>
  <span class="team">Meet Our Team</span>
</section>

<h2 class="abs shead" style="top:1862px">OUR SERVICES</h2>
<p class="abs serv-sub">Quisque posuere rhoncus erat, sit amet aliquet augue. Donec eros massa, gravida ac lectus et, pharetra interdum lectus.</p>

<div class="abs service" style="left:71px">
  <div class="img" role="img" aria-label="Photo of hands working on a laptop with financial papers" style="background:linear-gradient(135deg,#e9ecef,#9aa2a8 60%,#55606a)"></div>
  <div class="circ"><svg width="34" height="32" viewBox="0 0 34 32"><path d="M17 2L2 10h30z" fill="#fff"/><rect x="5" y="12" width="4" height="13" fill="#fff"/><rect x="15" y="12" width="4" height="13" fill="#fff"/><rect x="25" y="12" width="4" height="13" fill="#fff"/><rect x="2" y="27" width="30" height="3" fill="#fff"/></svg></div>
  <p class="lead">Focusing on your business – not on banking</p>
  <h3>What Banks Want</h3>
  <p>Even in today's information age, it is exceedingly difficult to keep up with changes.</p>
  <span class="btn">Read More</span>
</div>
<div class="abs service" style="left:346px">
  <div class="img" role="img" aria-label="Photo of a team meeting around a table" style="background:linear-gradient(135deg,#f1ece6,#c8b7a6 55%,#8a7a6c)"></div>
  <div class="circ"><svg width="36" height="30" viewBox="0 0 36 30"><circle cx="18" cy="8" r="5" fill="#fff"/><circle cx="7" cy="10" r="4" fill="#fff"/><circle cx="29" cy="10" r="4" fill="#fff"/><path d="M10 28c0-8 3-12 8-12s8 4 8 12zM0 26c0-6 3-9 7-9s6 3 6 9zM23 26c0-6 2-9 6-9s7 3 7 9z" fill="#fff"/></svg></div>
  <p class="lead">Focusing on your business – not on banking</p>
  <h3>Augment Your Team</h3>
  <p>Even in today's information age, it is exceedingly difficult to keep up with changes.</p>
  <span class="btn">Read More</span>
</div>
<div class="abs service" style="left:620px">
  <div class="img" role="img" aria-label="Illustration of a compass pointing toward profits" style="background:linear-gradient(135deg,#eef0f1,#b8bfc4 55%,#c44 100%)"></div>
  <div class="circ"><svg width="32" height="32" viewBox="0 0 32 32"><circle cx="15" cy="17" r="11" fill="none" stroke="#fff" stroke-width="2.5"/><path d="M15 11v12M18 13h-4.5a2 2 0 000 4h3a2 2 0 010 4H12" stroke="#fff" stroke-width="2" fill="none"/><path d="M22 2h8v8M30 2l-7 7" stroke="#fff" stroke-width="2.5" fill="none"/></svg></div>
  <p class="lead">Focusing on your business – not on banking</p>
  <h3>Understand Profitability</h3>
  <p>Even in today's information age, it is exceedingly difficult to keep up with changes.</p>
  <span class="btn">Read More</span>
</div>
<div class="abs service" style="left:889px">
  <div class="img" role="img" aria-label="Illustration of a businessman facing a wall of market charts" style="background:linear-gradient(135deg,#f4f4f4,#cfd3d6 55%,#8c949a)"></div>
  <div class="circ"><svg width="32" height="30" viewBox="0 0 32 30"><path d="M3 2h26l3 8H0z" fill="#fff"/><rect x="3" y="12" width="26" height="16" fill="#fff"/><rect x="8" y="16" width="6" height="12" fill="#a3180b"/><rect x="18" y="16" width="7" height="6" fill="#a3180b"/></svg></div>
  <p class="lead">Focusing on your business – not on banking</p>
  <h3>Know The Market</h3>
  <p>Even in today's information age, it is exceedingly difficult to keep up with changes.</p>
  <span class="btn">Read More</span>
</div>

<section class="abs clients">
  <h2>WORDS FROM OUR CLIENTS</h2>
  <p class="tag">Our ability to love ourselves and the world is endless and powerful</p>
  <div class="avatar" role="img" aria-label="Portrait photo of the client"></div>
  <p class="say">Lorem ipsum dolor sit amet, consectetur adipiscing elit. Donec lacus nibh, vulputate eu diam non, sodales Donec lacus nibh, vulputate eu diam non,</p>
  <p class="who">Marren Olsby</p>
  <p class="role">Dorian K. Halvers, Business Program Manager, <span>Northfield Civic Works</span></p>
  <div class="dots"><i></i><i></i><i class="on"></i><i></i></div>
</section>
<section class="abs feedback">
  <h2>We welcome any and all feedback</h2>
  <p>Lorem ipsum dolor sit amet, consectetur adipiscing elit, ulate eu diam Pellentesque molestie nisl in dolor gravida commodo. Lorem ipsum dolor sit amet</p>
  <div class="field first">Name</div>
  <div class="field">Your Email</div>
  <div class="field area">Your Message</div>
  <div class="send">Submit</div>
</section>

<footer class="abs footer">
  <div class="fcol" style="left:79px;width:240px">
    <h4>About Us</h4>
    <p>Aquam est tortor, sagittis in fringilla in, pellent esque nec erat. Aenean semper, neque non faucibus. tortor, sagittis in fringilla in, pellent esque nec eratsemper, neque non.</p>
  </div>
  <div class="fcol" style="left:406px">
    <h4>Our Services</h4>
    <ul><li>Website Builder</li><li>Web Design</li><li>Logo Design</li><li>Register Domains</li><li>Traffic Booster</li><li>Search Advertising</li></ul>
  </div>
  <div class="fcol" style="left:619px">
    <h4>Ask Your Question</h4>
    <div class="inp">Your Email</div>
    <div class="inp tall">Message</div>
    <div class="send">Send</div>
  </div>
  <div class="fcol" style="left:910px;width:220px">
    <h4>Contact Us</h4>
    <p>Harbrook is a great start for an education personnel or organization to start the online business with 1 Click.</p>
    <div class="crow"><svg width="16" height="14" viewBox="0 0 16 14"><rect x="1" y="2" width="14" height="10" fill="none" stroke="#4aa3df" stroke-width="1.5"/><path d="M1 2l7 6 7-6" stroke="#4aa3df" stroke-width="1.5" fill="none"/></svg>hello@harbrook.example</div>
    <div class="crow"><svg width="16" height="16" viewBox="0 0 16 16"><path d="M3 1l3 3-2 2c1 2 3 4 5 5l2-2 3 3-2 3C7 15 1 9 1 3z" fill="#4aa3df"/></svg>P: 555 010 482</div>
    <div class="crow"><svg width="16" height="18" viewBox="0 0 16 18"><path d="M8 17S2 10 2 7a6 6 0 0112 0c0 3-6 10-6 10z" fill="#4aa3df"/><circle cx="8" cy="7" r="2" fill="#1f1f1f"/></svg>42 Quillon Ave - Suite 300<br>United States - ZZ 00000</div>
  </div>
</footer>
<div class="abs copy">© 2016 qrvconsulting.example All Right Reserved.</div>

</body>
</html>
```